Business Card Design Project

I need the following:

Logo -
Name - Dale Prewitt
Title - Customer Experience Officer
Web - www.bvrh.net
Phone - 555-417-3068
Updates

Project Deadline Extended
Reason: I launched the project later than anticipated. I look forward to seeing your designs. Dale

Industry/Entity Type

Business

```html
<!DOCTYPE html>
<html lang="en">
<head>
<meta charset="utf-8">
<title>Dale Prewitt – Business Card</title>
<link href="https://fonts.googleapis.com/css2?family=Archivo:wght@800&family=Tinos:wght@400;700&display=swap" rel="stylesheet">
<style>
  :root {
    --backdrop: #e4e6e8;
    --card: #ffffff;
    --ink: #111316;
    --brand-blue: #1f8fd0;
    --mark-blue: #1d4f9c;
    --watermark: #eef1f5;
    --watermark-text: #e2e6ec;
    --rule-purple: #3b2f8f;
    --rule-warm: #f29a1e;
  }
  * { margin: 0; padding: 0; box-sizing: border-box; }
  html, body { width: 1200px; height: 898px; overflow: hidden; }
  body { background: var(--backdrop); position: relative; }

  .card {
    position: absolute;
    left: 130px; top: 180px;
    width: 940px; height: 537px;
    background: var(--card);
    box-shadow: 0 10px 30px rgba(0,0,0,0.18);
    overflow: hidden;
  }

  /* faint decorative backdrop on the right */
  .card__watermark {
    position: absolute;
    left: 520px; top: 20px;
    width: 260px; height: 260px;
    border-radius: 50%;
    background: var(--watermark);
  }
  .card__watermark-name {
    position: absolute;
    left: 520px; top: 118px;
    width: 260px;
    text-align: center;
    font: 800 56px/1 "Archivo", sans-serif;
    color: var(--watermark-text);
    letter-spacing: 2px;
  }

  /* company identity */
  .identity {
    position: absolute;
    left: 55px; top: 195px;
    display: flex; align-items: center; gap: 22px;
  }
  .identity__dot {
    width: 118px; height: 118px; border-radius: 50%;
    background: var(--mark-blue);
    flex: none;
  }
  .identity__name {
    font: 800 33px/30px "Archivo", sans-serif;
    color: var(--ink);
    text-transform: uppercase;
    letter-spacing: 0.5px;
  }
  .identity__web {
    display: flex; align-items: center; gap: 8px;
    margin-top: 6px;
    font: 700 14px/1 "Archivo", sans-serif;
    color: var(--brand-blue);
  }
  .identity__web::before, .identity__web::after {
    content: ""; flex: 1; height: 2px; background: var(--brand-blue);
  }

  /* person */
  .person {
    position: absolute;
    right: 80px; top: 232px;
    text-align: right;
  }
  .person__name {
    font: 700 31px/1 "Tinos", serif;
    color: var(--ink);
    text-transform: uppercase;
    letter-spacing: 1.5px;
    margin-right: 30px;
  }
  .person__title {
    margin-top: 12px;
    font: 400 27px/1 "Tinos", serif;
    color: var(--brand-blue);
    letter-spacing: 0.8px;
  }
  .contact {
    position: absolute;
    right: 80px; top: 330px;
    text-align: right;
    font: 700 19px/28px "Tinos", serif;
    color: var(--ink);
    letter-spacing: 0.5px;
  }

  .card__rule {
    position: absolute;
    left: 0; right: 0; top: 470px;
    height: 3px;
    background: linear-gradient(90deg, var(--rule-purple) 0%, var(--rule-purple) 55%, var(--rule-warm) 62%, var(--rule-purple) 70%, var(--rule-purple) 100%);
  }
</style>
</head>
<body>
  <section class="card" aria-label="Business card for Dale Prewitt">
    <div class="card__watermark" aria-hidden="true"></div>
    <div class="card__watermark-name" aria-hidden="true">BVRH</div>

    <div class="identity">
      <div class="identity__dot" aria-hidden="true"></div>
      <div>
        <div class="identity__name">Broadview<br>Relay<br>Holdings</div>
        <div class="identity__web">www.bvrh.net</div>
      </div>
    </div>

    <div class="person">
      <h1 class="person__name">Dale Prewitt</h1>
      <p class="person__title">Customer Experience Officer</p>
    </div>

    <div class="contact">
      <p class="contact__phone">555-417-3068</p>
      <p class="contact__web">www.bvrh.net</p>
    </div>

    <div class="card__rule" aria-hidden="true"></div>
  </section>
</body>
</html>
```